Profesional personal website needs design and business card

I need a business card with my professional name as a logo "Marlo Vitality" for my business. I am a Wellness Coach, consultant and trainer. So it should be professional, wellness oriented and modern.

Target Market(s)

Private clients, governments, corporations. Luxury and high market.

Industry/Entity Type

Health And Wellness

Contact Information for Business Card

Marlo Vitality should be the logo

Colors

Designer to choose colors to be used in the design.

Requirements
Must have
• Marlo Vitality
• Name: Tomás Arribal
• Wellness Coach, Consultant & Trainer.
• Website: www.marlovitality.example
• Phone:
• Spain (+34) 612 480 397
• (USA) +1 (555) 318 2046
Nice to have
• The most important is the design of "Marlo Vitality", as this is going to be my personal brand logo. It should be professional, wellness, high end and actual.
Should not have
• no golds, no baroque style..

```html
<!DOCTYPE html>
<html lang="en">
<head>
<meta charset="utf-8">
<title>Marlo Vitality – Business Card</title>
<link rel="stylesheet" href="https://fonts.googleapis.com/css2?family=Mulish:wght@400;500;600;800&display=swap">
<style>
  :root {
    --page: #ffffff;
    --card: #282828;
    --green: #6abf45;
    --white: #ffffff;
    --muted: #d6d6d6;
  }
  * { box-sizing: border-box; margin: 0; padding: 0; }
  html, body {
    width: 1026px;
    height: 1200px;
    overflow: hidden;
    background: var(--page);
    font-family: "Mulish", sans-serif;
  }
  .canvas { position: relative; width: 1026px; height: 1200px; }

  .card {
    position: absolute;
    background: var(--card);
  }
  .card--front {
    left: 31px; top: 34px; width: 962px; height: 550px;
    border-left: 8px solid var(--green);
    border-top: 7px solid var(--green);
  }
  .card--back {
    left: 32px; top: 622px; width: 962px; height: 552px;
    border-left: 8px solid var(--green);
    border-bottom: 7px solid var(--green);
  }

  .brand {
    position: absolute;
    left: 0; right: 0;
    display: flex;
    align-items: center;
    justify-content: center;
    gap: 12px;
    color: var(--white);
    font-weight: 600;
    letter-spacing: 0.02em;
    white-space: nowrap;
  }
  .brand__dot {
    border-radius: 50%;
    background: var(--green);
    flex: none;
  }
  .card--front .brand { top: 68px; font-size: 44px; }
  .card--front .brand__dot { width: 16px; height: 16px; }
  .card--back .brand { top: 230px; font-size: 72px; gap: 18px; }
  .card--back .brand__dot { width: 26px; height: 26px; }

  .person {
    position: absolute;
    left: 80px; top: 240px;
  }
  .person__name {
    color: var(--green);
    font-size: 45px;
    font-weight: 800;
    letter-spacing: 0.02em;
    line-height: 1;
  }
  .person__role {
    margin-top: 12px;
    color: var(--muted);
    font-size: 16px;
    letter-spacing: 0.05em;
    display: flex;
    align-items: center;
    gap: 8px;
  }
  .person__role-sep {
    display: inline-block;
    width: 2px; height: 22px;
    background: var(--muted);
  }

  .divider {
    position: absolute;
    left: 491px; top: 222px;
    width: 3px; height: 118px;
    background: var(--green);
  }

  .contact {
    position: absolute;
    left: 560px; width: 360px; top: 188px;
    text-align: center;
    color: var(--muted);
  }
  .contact__icon { width: 46px; height: 46px; display: block; margin: 0 auto 14px; }
  .contact__line { font-size: 23px; line-height: 42px; letter-spacing: 0.01em; }

  .web-band {
    position: absolute;
    left: 0; right: 0; top: 472px; height: 32px;
    background: var(--green);
    color: var(--white);
    font-size: 22px;
    letter-spacing: 0.08em;
    text-align: center;
    line-height: 32px;
  }
</style>
</head>
<body>
<main class="canvas">

  <section class="card card--front">
    <div class="brand"><span class="brand__dot"></span>Marlo Vitality</div>

    <div class="person">
      <h1 class="person__name">Tomás Arribal</h1>
      <p class="person__role">Wellness Coach <span class="person__role-sep"></span> Consultant &amp; Trainer</p>
    </div>

    <div class="divider"></div>

    <div class="contact">
      <svg class="contact__icon" viewBox="0 0 24 24" aria-hidden="true">
        <path fill="#6abf45" transform="rotate(-10 12 12)" d="M6.6 10.8c1.4 2.8 3.8 5.1 6.6 6.6l2.2-2.2c.3-.3.7-.4 1-.2 1.1.4 2.3.6 3.6.6.6 0 1 .4 1 1V20c0 .6-.4 1-1 1C10.6 21 3 13.4 3 4c0-.6.4-1 1-1h3.5c.6 0 1 .4 1 1 0 1.3.2 2.5.6 3.6.1.3 0 .7-.2 1l-2.3 2.2z"/>
      </svg>
      <p class="contact__line">Spain (+34) 612 480 397</p>
      <p class="contact__line">(USA) +1 (555) 318 2046</p>
    </div>

    <div class="web-band">www.marlovitality.example</div>
  </section>

  <section class="card card--back">
    <div class="brand"><span class="brand__dot"></span>Marlo Vitality</div>
  </section>

</main>
</body>
</html>
```